Liquor Label / Aguardiente

Label design for liquor bottle. Designers may submit multiple submissions.

Product Description:
Name: Viento de Plata™
Alcohol Category: Aguardiente (which in Spanish most closely translates to “burning water”) – aguardiente is derived from
cane sugar and is a general term for a type of alcoholic spirit in many Central and South America countries.
Taste: A smooth liquor with a comfortable yet spicy finish
Smell: Subtle aroma of spicy jalapeños
Liquid Color: Clear
Bottle Color: Clear
See link for reference - http://www.kelvostamp.com/sites/default/files/styles/uc_product_full/public/Pemrow_0.jpg?itok=9QmT2xLp
Closure: Bar top / cork
Bottle Shape/Size: height = 8.67in; diameter of base = 3.70in; diameter of neck = 0.85in

Label may consist of two separate parts (i.e. front and back, front and vertical side), or one continuous label.

Designer has complete freedom with color, font etc. unless otherwise stated below. The label MUST
contain (but is not limited only to) the following text exactly as written in quotes below:
- “Viento de Plata”
- “Aguardiente”
- “Cane Neutral Spirit with Natural Flavors”
- “35% Alc./Vol.”
- “750 ml”
- “Bottled by WP Spirits, LLC” and “Nashville, TN” - “Government Warning: (1) According to the Surgeon General, women should not drink alcoholic beverages during
pregnancy because of the risk of birth defects. (2) Consumption of alcoholic beverages impairs your ability to
drive a car or operate machinery, and may cause health problems.” (text in previous quotes must be in all
capitalized letters, text must be 2 MM in height and quote must be separated 2MM by all other text)
- Must be dedicated empty space for bar code (approximately 0.75in. height x 1.25in. length)

Target Market(s)

Label should have mass market appeal.
Age: 21 – 28 years old (primary target market is 21+ year old college students and recent graduates)
Target Market Gender: Both male and female, with emphasis on male
Consumption Focus: Spirit will be consumed typically as a shot, primarily at bars and secondarily off premise (label design will be critical for making our product highly visible behind a bar)
Marketing Theme: South American elements. The official Viento de Plata mascot is a llama and the incorporation and use of a llama somewhere (however large or small) on the bottle is encourage but by no means required.

Industry/Entity Type

Health

Requirements
Should not have
• Elements that may lead a potential consumer to believe the beverage is a craft liquor or an artisan brand. Please do not include images of peppers.

```html
<!DOCTYPE html>
<html lang="en">
<head>
<meta charset="utf-8">
<title>Viento de Plata – Aguardiente Labels</title>
<link rel="stylesheet" href="https://fonts.googleapis.com/css2?family=Kaushan+Script&family=Advent+Pro:wght@500&display=swap">
<style>
  :root {
    --page-bg: #f2f2f2;
    --label-bg: #4b3d35;
    --frame-orange: #f7941d;
    --frame-deep: #f26522;
    --title-gold: #f9b233;
    --text-orange: #f8a63a;
    --barcode-white: #ffffff;
  }
  * { margin: 0; padding: 0; box-sizing: border-box; }
  html, body {
    width: 1200px;
    height: 960px;
    overflow: hidden;
    background: var(--page-bg);
  }
  .canvas {
    position: relative;
    width: 1200px;
    height: 960px;
  }
  .label {
    position: absolute;
    top: 275px;
    width: 357px;
    height: 413px;
    border-radius: 20px;
    background: linear-gradient(135deg, var(--frame-orange), var(--frame-deep));
    padding: 8px;
    box-shadow: 0 3px 8px rgba(0,0,0,0.25);
  }
  .label-inner {
    position: relative;
    width: 100%;
    height: 100%;
    border-radius: 13px;
    background: var(--label-bg);
  }
  .label--front { left: 208px; }
  .label--back { left: 635px; }

  .brand-name {
    font-family: "Kaushan Script", cursive;
    font-weight: 400;
    color: var(--title-gold);
    text-align: center;
    position: absolute;
    left: 0; right: 0;
    line-height: 1;
  }
  .label--front .brand-name { top: 40px; font-size: 42px; }
  .label--back .brand-name { top: 30px; font-size: 34px; }

  .category {
    position: absolute;
    left: 0; right: 0;
    top: 99px;
    text-align: center;
    font-family: "Kaushan Script", cursive;
    font-size: 26px;
    color: var(--text-orange);
    line-height: 1;
  }
  .spirit-type {
    position: absolute;
    left: 0; right: 0;
    top: 144px;
    text-align: center;
    font-family: "Kaushan Script", cursive;
    font-size: 15px;
    color: var(--text-orange);
  }
  .band {
    position: absolute;
    left: -8px;
    right: -8px;
    top: 223px;
    height: 52px;
    background: linear-gradient(90deg, var(--frame-orange) 0%, #f99d2a 55%, var(--frame-deep) 100%);
  }
  .emblem {
    position: absolute;
    left: 110px;
    top: 184px;
    width: 116px;
    height: 116px;
  }
  .volume, .strength {
    position: absolute;
    bottom: 22px;
    font-family: "Kaushan Script", cursive;
    font-size: 16px;
    color: var(--text-orange);
  }
  .volume { left: 35px; }
  .strength { right: 24px; }

  .bottler {
    position: absolute;
    left: 0; right: 0;
    top: 84px;
    text-align: center;
    font-family: "Kaushan Script", cursive;
    font-size: 13px;
    line-height: 16px;
    color: var(--text-orange);
  }
  .gov-warning {
    position: absolute;
    left: 29px;
    top: 145px;
    width: 310px;
    font-family: "Advent Pro", sans-serif;
    font-weight: 500;
    font-size: 15px;
    line-height: 16px;
    color: var(--text-orange);
    text-transform: uppercase;
  }
  .barcode-space {
    position: absolute;
    left: 165px;
    top: 287px;
    width: 144px;
    height: 86px;
    background: var(--barcode-white);
  }
</style>
</head>
<body>
<div class="canvas">

  <section class="label label--front">
    <div class="label-inner">
      <h1 class="brand-name">Viento de Plata</h1>
      <p class="category">Aguardiente</p>
      <p class="spirit-type">Cane Neutral Spirit with Natural Flavors</p>
      <div class="band"></div>
      <svg class="emblem" viewBox="0 0 116 116">
        <defs>
          <linearGradient id="emblem-ring" x1="0" y1="0" x2="1" y2="1">
            <stop offset="0" stop-color="#f9a83a"/>
            <stop offset="1" stop-color="#f26522"/>
          </linearGradient>
          <radialGradient id="emblem-fill" cx="0.5" cy="0.55" r="0.55">
            <stop offset="0" stop-color="#c8612a"/>
            <stop offset="1" stop-color="#4b3d35"/>
          </radialGradient>
        </defs>
        <circle cx="58" cy="58" r="57" fill="url(#emblem-ring)"/>
        <circle cx="58" cy="58" r="48" fill="url(#emblem-fill)"
                role="img" aria-label="Brand emblem area: flame illustration"/>
      </svg>
      <p class="volume">750 ml</p>
      <p class="strength">35% Alc./Vol.</p>
    </div>
  </section>

  <section class="label label--back">
    <div class="label-inner">
      <h2 class="brand-name">Viento de Plata</h2>
      <p class="bottler">Bottled by WP Spirits, LLC<br>Nashville, TN</p>
      <p class="gov-warning">
        Government Warning: (1) According to the<br>
        Surgeon General, women should not drink<br>
        alcoholic beverages during<br>
        pregnancy because of the risk of birth<br>
        defects. (2) Consumption of alcoholic<br>
        beverages impairs your ability to<br>
        drive a car or operate machinery, and may<br>
        cause health problems.
      </p>
      <div class="barcode-space"></div>
    </div>
  </section>

</div>
</body>
</html>
```